Bramford Holloway Inc. needs an innovative idea for letterhead and visiting cards.

Bramford Holloway Inc. is a Canadian brand since 2007. It is a renown dealer of kids and office furniture locally. Moreover, exporting electric fixtures e.g. switches, LED's, down-lights etc. to Middle East and Africa. We have initiated a number of steps including re-branding, to boost our export in 2020. We have successfully designed our new logo a few months ago through 'Mockplanet' and now we are looking for an innovative idea for a letterhead.
Some key points:
• Red, black and white are the three colors used in all our packaging and furniture. (grey is optional)
• Shouldn’t be too wide.
• Use of watermark is preferable.
• You can visit our North American site at www.bramfordhollowayinc.com. Export website of the company will be launched soon. www.bramfordhollowayinc.ca
• Same letterhead will be used locally and internationally.
• Our new logo and sample packaging is attached.

```html
<!DOCTYPE html>
<html lang="en">
<head>
<meta charset="utf-8">
<title>Bramford Holloway Inc. — Business Card</title>
<link rel="stylesheet" href="https://fonts.googleapis.com/css2?family=Montserrat:wght@300;400;500&display=swap">
<style>
  :root {
    --backdrop: #161616;
    --card: #222222;
    --card-edge: #2c2c2c;
    --emboss: #6a6a6a;
    --red: #a4141b;
    --white: #f2f2f2;
  }
  * { box-sizing: border-box; margin: 0; padding: 0; }
  html, body { width: 1200px; height: 900px; overflow: hidden; }
  body {
    background: radial-gradient(ellipse at 50% 30%, #2a2a2a 0%, var(--backdrop) 70%);
    font-family: "Montserrat", sans-serif;
    position: relative;
  }
  .card {
    position: absolute;
    left: 250px;
    width: 700px;
    height: 400px;
    background: linear-gradient(135deg, var(--card) 0%, #1c1c1c 100%);
    border: 1px solid var(--card-edge);
    box-shadow: 0 14px 30px rgba(0,0,0,0.55);
  }
  .card-front { top: 40px; }
  .card-back { top: 470px; }

  /* Front: brand lockup */
  .brand-lockup {
    position: absolute;
    left: 130px;
    top: 130px;
    display: flex;
    align-items: center;
    gap: 22px;
  }
  .brand-square {
    width: 120px;
    height: 120px;
    border: 4px solid var(--emboss);
    border-radius: 12px;
  }
  .brand-name {
    color: var(--emboss);
    font-weight: 300;
    font-size: 46px;
    line-height: 1.05;
    letter-spacing: 3px;
    text-transform: uppercase;
  }

  /* Back: contact side */
  .badge {
    position: absolute;
    left: 60px;
    top: 95px;
    width: 210px;
    height: 210px;
    border: 10px solid var(--red);
    border-radius: 22px;
  }
  .divider {
    position: absolute;
    left: 310px;
    top: 80px;
    width: 2px;
    height: 240px;
    background: var(--red);
  }
  .contact {
    position: absolute;
    left: 340px;
    top: 80px;
    color: var(--white);
    font-weight: 400;
    font-size: 19px;
    line-height: 1.35;
  }
  .person-name {
    color: var(--red);
    font-weight: 300;
    font-size: 25px;
    letter-spacing: 3px;
    text-transform: uppercase;
  }
  .person-role { margin-bottom: 18px; }
  .address { margin-bottom: 12px; }
  .contact-line {
    display: flex;
    align-items: center;
    gap: 10px;
    margin-left: -26px;
  }
  .contact-line svg { width: 16px; height: 16px; flex: none; }
  .domain { color: var(--red); }
</style>
</head>
<body>
  <section class="card card-front">
    <div class="brand-lockup">
      <div class="brand-square"></div>
      <div class="brand-name">Bramford<br>Holloway</div>
    </div>
  </section>

  <section class="card card-back">
    <div class="badge"></div>
    <div class="divider"></div>
    <div class="contact">
      <p class="person-name">Marcus Ellery</p>
      <p class="person-role">Director</p>
      <p class="address">48 Harwell Ave,<br>Unit 207, Oakridge</p>
      <p class="contact-line">
        <svg viewBox="0 0 16 16" aria-hidden="true"><path d="M4 1 L6 5 L4.5 6.5 C5.5 8.8 7.2 10.5 9.5 11.5 L11 10 L15 12 L14 15 C7 15 1 9 1 2 Z" fill="none" stroke="#a4141b" stroke-width="1.3"/></svg>
        <span>+1 (888) 555-0142</span>
      </p>
      <p class="contact-line">
        <svg viewBox="0 0 16 16" aria-hidden="true"><rect x="1" y="3" width="14" height="10" fill="none" stroke="#a4141b" stroke-width="1.3"/><path d="M1 3 L8 9 L15 3" fill="none" stroke="#a4141b" stroke-width="1.3"/></svg>
        <span>sales@bramfordhollowayinc.com</span>
      </p>
      <p class="contact-line">
        <svg viewBox="0 0 16 16" aria-hidden="true"><circle cx="8" cy="8" r="6.5" fill="none" stroke="#a4141b" stroke-width="1.3"/><ellipse cx="8" cy="8" rx="3" ry="6.5" fill="none" stroke="#a4141b" stroke-width="1.1"/><path d="M1.5 8 H14.5" stroke="#a4141b" stroke-width="1.1"/></svg>
        <span>www.<span class="domain">bramfordhollowayinc</span>.com</span>
      </p>
    </div>
  </section>
</body>
</html>
```